A resource brochure for seniors and their families/Maplecrest Resource Group

As we age, the journey can come with unexpected challenges and obstacles. Maplecrest Resource Group is here to provide seniors and their families with a road map to navigate those challenges and insure the journey is as smooth as possible. We are a company that offers 'one stop shop' resources for seniors who need assistance with selling their home, need home care support or need to find suitable senior housing living choices and much more. We need this brochure to showcase a caring, clear and clear way for families or individuals, many who have just lost a spouse/parent, to find resources during a very difficult and confusing time in their life. The final design should communicate caring support, a call to action (call us!), and showcase a professional and knowledgeable team that will gently support and be a guide to families and individuals who are trying to make big life choices within the senior care arena.
Updates

Project Deadline Extended Reason: To give more time for designers as the initial window seemed a little too short. Thank you!!! Added Friday, March 20, 2015

Target Market(s)

A mature market- SENIORS (75+) and their families (adult children 50+) who typically are going through life changes such as losing a spouse or having to make a move from their home into a Retirement Community.

Industry/Entity Type

Group

Font styles to use
Serif
Script

Requirements
Must have
• Showcase a thoughtful and caring mentality- 'we will take care of you" in a professional and knowledgeable way. Please make it clear what the message is - we can assist with selling a home, bringing support and care into the home, find more appropriate housing as well as any resources or tools needed throughout the senior care spectrum of resources. Must have our name, logo, website and address and we need one panel to be laid out as a mailer- our address on top left. (Please see attached rough draft for address- thank you!) Also- please keep the testimonial, which is attached inclusive of additional verbiage.
Nice to have
• An attractive senior (female) on the cover of the brochure with a 'What's Next?" feel to engage people to open the collateral and relate to the story and purpose of what we do. Showcase what our services are- we are a company that guides families to and through much needed resources as it relates to aging and the ever-changing needs of an elderly person. We want to be the experts and trusted by our clients and the tough decisions that come along with aging. We offer our referral services at no cost to our clients.
Should not have
• Should not sound slick, 'sales-y' or too pushy- we are trying to build a relationship and not 'over sell'...we want to be a trusted resource guide and a helping hand.

```html
<!DOCTYPE html>
<html lang="en">
<head>
<meta charset="utf-8">
<title>Maplecrest Resource Group – Brochure</title>
<link rel="stylesheet" href="https://fonts.googleapis.com/css2?family=Fira+Sans:ital,wght@0,600;0,700;1,600;1,800&family=Source+Sans+3:ital,wght@0,400;0,600;0,700;1,600&display=swap">
<style>
:root{
  --stage:#3d3029;
  --slate:#4b5272;
  --ink:#3a3f5c;
  --body:#6b6e7a;
  --green:#8dc63f;
  --orange:#f7b21f;
  --cream:#fdf3dc;
  --cream-soft:#fef7e8;
  --white:#ffffff;
}
*{box-sizing:border-box;margin:0;padding:0}
html,body{width:1000px;height:1200px;overflow:hidden}
body{background:var(--stage);position:relative;font-family:"Source Sans 3",Arial,sans-serif;color:var(--body)}
.sheet{position:absolute;background:var(--white);box-shadow:0 4px 14px rgba(0,0,0,.45);overflow:hidden}
.sheet--outside{left:38px;top:25px;width:812px;height:573px}
.sheet--inside{left:148px;top:607px;width:810px;height:573px}
.abs{position:absolute}
.photo{position:absolute}
.panel-tab{position:absolute;height:22px;font:700 11px "Source Sans 3",Arial,sans-serif;color:var(--white);padding:4px 10px}
.brand{display:flex;align-items:center;gap:6px;font:600 13px "Source Sans 3",Arial,sans-serif;color:var(--ink)}
.brand__dot{width:11px;height:11px;border-radius:50%;background:var(--orange);flex:none}

/* outside: testimonial */
.testimonial-box{left:0;top:333px;width:270px;height:230px;background:var(--slate);color:var(--white);padding:10px 10px}
.testimonial-box .mark{font:800 70px/0.9 "Fira Sans",Arial,sans-serif;height:46px}
.testimonial-box p{font-size:10.2px;line-height:12.4px;font-weight:600}
.testimonial-box .by{font-style:italic;font-weight:700;margin-top:8px}

/* outside: contact */
.contact{left:270px;top:22px;width:272px;height:278px;text-align:center}
.contact .brand{justify-content:center;margin-top:150px;font-size:14px}
.contact dl{margin-top:14px;font-size:10.5px;line-height:15px;color:var(--ink)}
.contact dt{display:inline;font-weight:700;font-style:italic}
.contact dd{display:inline}

/* outside: cover */
.cover{left:542px;top:0;width:270px;height:573px;background:var(--cream)}
.cover .brand{position:absolute;left:28px;top:20px;font-size:11px}
.cover h1{position:absolute;left:12px;top:54px;font:800 italic 26px "Fira Sans",Arial,sans-serif;color:var(--slate);letter-spacing:-.3px}

/* inside */
.hands-band{left:0;top:0;width:810px;height:130px}
.intro{left:0;top:80px;width:272px;height:276px;background:var(--cream-soft);padding:20px 10px 0}
.intro .brand{font-size:11px;margin-bottom:10px}
h2{font:700 10px "Source Sans 3",Arial,sans-serif;color:var(--ink);margin-bottom:2px}
.copy{font-size:8.6px;line-height:11.4px;color:var(--body)}
.copy p+h2,.copy ul+h2,.copy p+p{margin-top:7px}
.copy ul{list-style:none}
.copy li{padding-left:14px;position:relative}
.copy li::before{content:"•";position:absolute;left:2px}
.services{left:286px;top:136px;width:260px}
.how{left:549px;top:290px;width:252px}
.quote-area{left:0;top:353px;width:272px;height:212px;background:var(--cream-soft)}
.quote-area blockquote{position:absolute;right:12px;top:14px;width:120px;text-align:right;font:600 italic 11px/13.6px "Source Sans 3",Arial,sans-serif;color:var(--ink)}
.quote-area .mark{font:800 48px/0.8 "Fira Sans",Arial,sans-serif;color:var(--slate);height:30px;margin-right:18px}
.quote-area cite{display:block;margin-top:6px;font-size:9px;font-weight:400;color:var(--body)}
.divider{position:absolute;top:135px;width:1px;height:220px;background:#e3e3e3}
</style>
</head>
<body>

<section class="sheet sheet--outside" aria-label="Brochure outside">
  <!-- Testimonial panel -->
  <div class="panel-tab" style="left:0;top:0;width:270px;background:var(--green)">Testimonial</div>
  <div class="photo" role="img" aria-label="Young caregiver smiling with an elderly woman in a wheelchair" style="left:0;top:22px;width:270px;height:311px;background:linear-gradient(135deg,#d9cbbd,#b9a38f 45%,#6f88a8)"></div>
  <div class="abs testimonial-box">
    <div class="mark">&ldquo;</div>
    <p>After Dad passed, the team at Maplecrest came to the rescue.<br>We really appreciate the resources and time Marcus spent with us as we as a family were experiencing such a difficult time, a loss of my Dad and needing to find a new home for Mom.<br>I highly recommend your services and by the way, Mom loves her new community and has made several friends!&rdquo;</p>
    <p class="by">– Daniel, Kirkland WA</p>
  </div>
  <div class="abs" style="left:0;top:563px;width:270px;height:10px;background:var(--green)"></div>

  <!-- Contact panel -->
  <div class="panel-tab" style="left:270px;top:0;width:272px;background:var(--orange)">Contact information</div>
  <div class="abs contact">
    <div class="brand"><span class="brand__dot"></span>Maplecrest Resource Group</div>
    <dl>
      <dt>Call:</dt> <dd>(800) 555-0142</dd><br>
      <dt>Email:</dt> <dd>hello@maplecrestRG.com</dd><br>
      <dt>Address:</dt> <dd>4820 Alder Lane</dd><br>
      <dd>Suite C104 Edgewood, WA 98372</dd>
    </dl>
  </div>
  <div class="photo" role="img" aria-label="Group of cheerful seniors giving thumbs up" style="left:270px;top:300px;width:272px;height:263px;background:linear-gradient(160deg,#e9e4dd,#cdb8a4 50%,#8fa6c2)"></div>
  <div class="abs" style="left:270px;top:563px;width:272px;height:10px;background:var(--orange)"></div>

  <!-- Cover panel -->
  <div class="abs cover">
    <div class="brand"><span class="brand__dot"></span>Maplecrest Resource Group</div>
    <h1>What do I do now?</h1>
    <svg class="abs" style="left:0;top:0" width="270" height="573" viewBox="0 0 270 573" aria-hidden="true">
      <path d="M40 150 A150 150 0 0 0 90 395 A140 140 0 0 1 40 150Z" fill="var(--green)"/>
      <path d="M230 380 A118 118 0 0 1 230 573 L250 573 A130 130 0 0 0 230 380Z" fill="var(--orange)"/>
      <path d="M235 380 A122 122 0 0 1 270 460 L270 400Z" fill="var(--green)"/>
      <circle cx="150" cy="245" r="148" fill="var(--white)"/>
      <circle cx="120" cy="470" r="118" fill="var(--white)"/>
    </svg>
    <div class="photo" role="img" aria-label="Thoughtful elderly man resting his chin on his hand" style="left:8px;top:103px;width:284px;height:284px;border-radius:50%;background:radial-gradient(circle at 45% 45%,#e6c3ad,#b98f78 55%,#8a9aa7)"></div>
    <div class="photo" role="img" aria-label="Smiling senior couple cheek to cheek" style="left:7px;top:357px;width:226px;height:226px;border-radius:50%;background:radial-gradient(circle at 40% 50%,#f0d3bf,#cfa98d 55%,#9db3c6)"></div>
  </div>
</section>

<section class="sheet sheet--inside" aria-label="Brochure inside">
  <div class="photo hands-band" role="img" aria-label="Close-up of an elderly hand held gently in a younger hand" style="background:linear-gradient(90deg,#4d78b0,#8fa7c7 30%,#d8b9a3 55%,#b9a693 80%,#e7a24a)"></div>
  <svg class="abs" style="left:0;top:0" width="810" height="135" viewBox="0 0 810 135" aria-hidden="true">
    <path d="M0 22 C180 80 420 122 810 112 L810 135 L0 135Z" fill="var(--white)"/>
    <path d="M0 22 C180 80 420 122 810 112 L810 116 C420 126 180 86 0 28Z" fill="#9fb7d6"/>
    <path d="M0 28 C180 86 420 126 810 116 L810 135 L0 135Z" fill="var(--white)"/>
    <path d="M0 28 C120 68 200 84 272 94 L272 135 L0 135Z" fill="var(--cream-soft)"/>
  </svg>

  <div class="abs intro copy">
    <div class="brand" style="margin-top:8px"><span class="brand__dot"></span>Maplecrest Resource Group</div>
    <h2>A helping hand during life’s transitions…</h2>
    <p>During any major transition in life, we all could use a little help. We at Maplecrest are here to assist you during these times when it is easy to become overwhelmed and confused with ‘what’s next?’. Whatever the newest challenge or question that may arise, call Maplecrest and let us work with you to find your best path forward.</p>
    <h2 style="margin-top:7px">Our Mission…</h2>
    <p>What started as an informal network has grown into something exceptional. This network of dedicated professionals share the same values, integrity, and mission to serve our seniors and their families with the highest level of integrity possible. The goal, promise, and purpose of our network is to provide you with a simple and comprehensive path to help you navigate the challenges that arise as we all age. We look forward to serving you!</p>
  </div>

  <div class="divider" style="left:278px"></div>
  <div class="divider" style="left:540px"></div>

  <div class="abs services copy">
    <p>As we age there are always new questions that arise.<br>We at Maplecrest Resource Group have over 50 years of combined experience helping seniors and their families find their customized path to whatever comes next.</p>
    <h2 style="margin-top:14px">Need help with….</h2>
    <ul>
      <li>Preparing a home for sale</li>
      <li>Downsizing</li>
      <li>Home maintenance and remodeling for accessibility</li>
      <li>Selling a home</li>
      <li>Bringing support into the home</li>
      <li>Finding senior living options</li>
      <li>Financial planning</li>
      <li>Estate planning</li>
      <li>Funeral pre-planning</li>
      <li>Life insurance services</li>
      <li>Or anything else…</li>
    </ul>
  </div>

  <div class="photo" role="img" aria-label="Smiling senior couple embracing" style="left:549px;top:128px;width:240px;height:157px;background:linear-gradient(135deg,#e8eef4,#9a7a66 45%,#d9c6b8)"></div>
  <div class="abs how copy">
    <h2>How we work:</h2>
    <p>One of our local resource advisors will work one-on-one with you to fully understand your situation in order find and recommend the best path for you. Our plan for you can be as simple or as intricate as you would like or need.</p>
    <p>We are available to work:</p>
    <ul>
      <li>Over the phone</li>
      <li>Face-to-face</li>
      <li>Via email</li>
      <li>Or whatever makes you the most comfortable</li>
    </ul>
    <h2 style="margin-top:12px">What does this cost?</h2>
    <p>At Maplecrest RG we offer our planning and resource referral services at no charge to you and your family.</p>
    <h2 style="margin-top:12px">How do I get started?</h2>
    <p style="margin-top:0">Simply call (800) 555-0142<br>or email us at hello@maplecrestRG.com</p>
  </div>

  <div class="abs quote-area">
    <div class="photo" role="img" aria-label="Smiling senior woman with silver hair" style="left:0;top:0;width:140px;height:212px;background:linear-gradient(120deg,#d9d3cc,#8a624c 50%,#c7a58c)"></div>
    <blockquote>
      <div class="mark">&rdquo;</div>
      Never believe that a few caring people can’t change the world. For, indeed, that’s all who ever have.”
      <cite>- Ruth Ellison</cite>
    </blockquote>
  </div>

  <div class="photo" role="img" aria-label="Adviser reviewing documents with a couple on a sofa" style="left:284px;top:355px;width:244px;height:203px;background:linear-gradient(150deg,#f1efec,#b8b0a8 50%,#6f6a6a)"></div>

  <svg class="abs" style="left:0;top:490px" width="810" height="83" viewBox="0 0 810 83" aria-hidden="true">
    <path d="M0 83 L0 76 C300 78 560 50 810 14 L810 83Z" fill="var(--green)" opacity=".85"/>
    <path d="M0 76 C300 74 560 48 810 10 L810 18 C560 56 300 80 0 82Z" fill="var(--orange)"/>
    <path d="M0 70 C300 70 560 44 810 4 L810 10 C560 48 300 74 0 76Z" fill="var(--white)"/>
  </svg>
</section>

</body>
</html>
```